Business Card/Letterhead Design

We have our Logo, we simply need it cleaned up. Along with a letterhead design. It's pretty simple really.
Instead of the "Corporation" beside the logo. We need it to say "Limited" just under the logo between the "F" and the "Y"
The letter head has to have our address. 2745 Halvorby Crescent Mississauga, ON L4W 3K8 Canada
Reason: I have been called out of town until Monday of next week.
Business
Contact Information for Business Card
2745 Halvorby Crescent Mississauga, ON L4W 3K8 Canada

```html
<!DOCTYPE html>
<html lang="en">
<head>
<meta charset="utf-8">
<title>Larkstone Limited – Stationery</title>
<link href="https://fonts.googleapis.com/css2?family=Questrial&family=Montserrat:wght@400;600&display=swap" rel="stylesheet">
<style>
  :root{
    --backdrop:#eeeef0;
    --paper:#ffffff;
    --royal:#2d189e;
    --royal-deep:#22127e;
    --royal-light:#4a2fd0;
    --sand:#d6b796;
    --sand-light:#e8d3bd;
    --ink:#4a4a4f;
    --ink-soft:#77777d;
  }
  *{box-sizing:border-box;margin:0;padding:0}
  html,body{width:1200px;height:900px;overflow:hidden}
  body{background:var(--backdrop);font-family:"Questrial",sans-serif;color:var(--ink);position:relative}

  /* Letterhead */
  .letterhead{position:absolute;left:50px;top:24px;width:600px;height:850px;background:var(--paper);box-shadow:0 6px 24px rgba(0,0,0,.12);overflow:hidden}
  .letterhead__header{display:flex;justify-content:space-between;align-items:flex-start;padding:48px 44px 0 50px}
  .brand{display:flex;align-items:center;gap:8px;color:var(--royal);font-family:"Questrial",sans-serif}
  .brand__dot{width:12px;height:12px;border-radius:50%;background:var(--royal);flex:none}
  .brand__name{font-size:24px;letter-spacing:.5px;line-height:1}
  .contact{display:flex;gap:22px;font-size:7px;line-height:1.5;color:var(--ink-soft)}
  .contact__item{display:flex;gap:4px}
  .contact__bullet{width:4px;height:4px;border-radius:50%;background:var(--royal);margin-top:3px;flex:none}
  .letter{padding:46px 50px 0 80px;font-size:9.5px;line-height:1.5;color:var(--ink)}
  .letter p{margin-bottom:12px}
  .letter strong{font-family:"Montserrat",sans-serif;font-weight:600;color:#222}
  .letter__body{text-align:left}
  .letterhead__footer{position:absolute;left:0;bottom:0;width:600px;height:170px}

  /* Business card */
  .card{position:absolute;left:705px;top:250px;width:440px;height:252px;border-radius:3px;overflow:hidden;background:linear-gradient(135deg,var(--royal-light) 0%,var(--royal) 45%,var(--royal-deep) 100%);box-shadow:0 8px 22px rgba(0,0,0,.18)}
  .card__brand{position:absolute;left:0;right:0;top:70px;display:flex;justify-content:center;align-items:center;gap:10px;color:#fff}
  .card__brand .brand__dot{background:#fff;width:14px;height:14px}
  .card__brand .brand__name{font-size:30px}
  .card__band{position:absolute;left:0;top:0;width:440px;height:252px}
  .card__address{position:absolute;left:20px;bottom:14px;display:flex;align-items:center;gap:8px;font-size:12px;color:var(--royal-deep)}
  .pin{width:18px;height:18px;flex:none}

  /* Standalone mark */
  .signoff-brand{position:absolute;right:60px;bottom:60px}
  .signoff-brand .brand__name{font-size:34px}
  .signoff-brand .brand__dot{width:16px;height:16px}
</style>
</head>
<body>

<article class="letterhead">
  <header class="letterhead__header">
    <div class="brand">
      <span class="brand__dot"></span>
      <span class="brand__name">Larkstone Limited</span>
    </div>
    <div class="contact">
      <div>
        <div class="contact__item"><span class="contact__bullet"></span><span>Address: 2745 Halvorby Crescent<br>Mississauga, ON L4W 3K8<br>Canada</span></div>
        <div class="contact__item"><span class="contact__bullet"></span><span>www.larkstoneltd.com</span></div>
      </div>
      <div>
        <div class="contact__item"><span class="contact__bullet"></span><span>M: +1 905 555 0142<br>T: +1 905 555 0187</span></div>
        <div class="contact__item"><span class="contact__bullet"></span><span>hello@larkstoneltd.com</span></div>
      </div>
    </div>
  </header>

  <section class="letter">
    <p>To<br>The Manager<br>xyzxyz<br>abc city</p>
    <p>Dated - 17 Oct 2014</p>
    <p>Subject- <strong>Lorem Ipsum is simply dummy text of the printing and typesetting industry.</strong></p>
    <p>Sir</p>
    <div class="letter__body">
      <p>Lorem Ipsum is simply dummy text of the printing and typesetting industry. Lorem Ipsum has been the industry's standard dummy text ever since the 1500s, when an unknown printer took a galley of type and scrambled it to make a type specimen book. It has survived not only five centuries, but also the leap into electronic typesetting, remaining essentially unchanged. It was popularised in the 1960s with the release of printed transfer sheets containing Lorem Ipsum passages, and more recently with desktop publishing software, including common layout programs that ship versions of Lorem Ipsum.</p>
      <p>It is a long established fact that a reader will be distracted by the readable content of a page when looking at its layout. The point of using Lorem Ipsum is that it has a more-or-less normal distribution of letters, as opposed to using 'Content here, content here', making it look like readable English. Many desktop publishing packages and web page editors now use Lorem Ipsum as their default model text, and a search for 'lorem ipsum' will uncover many web sites still in their infancy. Various versions have evolved over the years, sometimes by accident, sometimes on purpose (injected humour and the like).</p>
      <p>Contrary to popular belief, Lorem Ipsum is not simply random text. It has roots in a piece of classical Latin literature from 45 BC, making it over 2000 years old. The point of using Lorem Ipsum is that it has a more-or-less normal distribution of letters, as opposed to using 'Content here, content here'.</p>
    </div>
    <p>Thanking You</p>
    <p>abcdef<br>xyz post<br>Larkstone</p>
  </section>

  <svg class="letterhead__footer" viewBox="0 0 600 170" preserveAspectRatio="none" aria-hidden="true">
    <path d="M0 170 L0 150 C180 148 400 100 600 30 L600 170 Z" fill="var(--sand)"/>
    <path d="M0 160 C200 150 420 100 600 45 L600 52 C420 110 210 156 0 166 Z" fill="#fff" opacity=".85"/>
    <path d="M60 140 C250 120 430 60 560 0 C440 70 260 128 60 140 Z" fill="var(--sand-light)"/>
  </svg>
</article>

<article class="card">
  <svg class="card__band" viewBox="0 0 440 252" aria-hidden="true">
    <path d="M0 252 L0 200 C150 198 320 185 440 140 L440 252 Z" fill="var(--sand)"/>
    <path d="M0 194 C150 190 310 176 440 128 L440 134 C310 182 150 196 0 200 Z" fill="var(--royal-light)"/>
  </svg>
  <div class="brand card__brand">
    <span class="brand__dot"></span>
    <span class="brand__name">Larkstone Limited</span>
  </div>
  <div class="card__address">
    <svg class="pin" viewBox="0 0 18 18" aria-hidden="true">
      <circle cx="9" cy="9" r="9" fill="var(--royal)"/>
      <path d="M9 4a3.2 3.2 0 0 0-3.2 3.2C5.8 9.8 9 14 9 14s3.2-4.2 3.2-6.8A3.2 3.2 0 0 0 9 4z" fill="#fff"/>
      <circle cx="9" cy="7.2" r="1.2" fill="var(--royal)"/>
    </svg>
    <span>2745 Halvorby Crescent Mississauga, ON L4W 3K8 Canada</span>
  </div>
</article>

<div class="brand signoff-brand">
  <span class="brand__dot"></span>
  <span class="brand__name">Larkstone Limited</span>
</div>

</body>
</html>
```